Flyer-Design - Coaching & Supervision für freib. Dipl.-Psychologin - BITTE KEINE WEITEREN DESINGS
Zielgruppe
--------- An alle, die überlegen mitzumachen - ich habe gerade als ungefähren Zeitplan, dass ich mich bis Donnerstag Abend (27.01.) entscheide, damit dann am Freitag (+evtl. Wochenende) noch Zeit für das Feintuning ist. -------------------
Ich bin Diplom-Psychologin und arbeite unter anderem freiberuflich als Coach und Supervisorin. Für diese Arbeit brauche ich einen Flyer. Ich habe bereits ein Konzept mit den Inhalten erstellt und brauche dafür nun ein professionelles Layout.
Aufgabenstellung
Anbei finden Sie das Konzept 1x als ppt (inklusive ausprobierter Alternativen zu den Fotos) und 1x als pdf.
Der Flyer hat als zentrales Thema „sich verändern / sich auf den Weg machen“ sowie die Analogie, dass ein gutes Coachinggespräch wie eine Bergtour ist.
Ich habe viel Vorarbeit gemacht (Inhalte stehen, Fotos sind recherchiert…) – sehr gerne können Sie sich kreativ ausleben und was völlig Neues / alles anders machen, es wäre aber auch ok, wenn das bereits Erarbeitete einfach graphisch aufgepimpt und professionalisiert wird.
Mein Wunsch: Ich weiß, dass der Flyer sehr voll ist. Aber ich möchte bewusst relativ viel Info dort unterbringen. Deshalb wäre es gut, wenn die Grafik des Flyers eine gewisse Leichtigkeit beinhaltet, die den vielen Text eher kaschiert. Also nicht zu verschnörkelt, sondern eher schlicht, hell und das Auge entlastend. Ich wünsche mir warme Farbtöne, die einladen und nicht zu kühl-modern wirken.
Logo:
Das Logo habe ich hier auf der Seite gestaltmarkt.de entwickeln lassen und habe alle Rechte daran. Es kann bei Bedarf auch angepasst werden.
Aktuell ist das Logo in grün, da ich dadurch den Naturbezug meiner Metapher mit aufgreife und weil die gerade entstehende Homepage, aktuell auch grün als Grundfarbe hat. Allerdings werde ich die Homepage auch noch professional überarbeiten lassen. Anbei einen Screenshot wie die Startseite der Homepage im Moment so ca. aussieht.
Bilder:
Die Fotos von mir hat ein Fotograf gemacht und ich darf sie verwenden.
Die Landschaftsbilder habe ich kostenlos und lizenzfrei von Lumora Bild ( https://bild.lumora-fotos.de/de/frei ) und von Fotelix ( https://fotelix-bilder.de/de/ ) heruntergeladen.
Falls Sie andere Bilder besser fänden und diese vorschlagen wollen, dann finden Sie weitere Details zu meinen Wünschen an die Bilder im Dokument „SelmK_AusschreibungDetails“
Die Landkarte ist ein Screenshot von KartoWeltNetz. Dort steht i..

```html
<!DOCTYPE html>
<html lang="de">
<head>
<meta charset="utf-8">
<title>Flyer Coaching &amp; Supervision</title>
<link href="https://fonts.googleapis.com/css2?family=Alegreya:ital,wght@0,400;0,500;1,400&family=Open+Sans:wght@400;600;700&display=swap" rel="stylesheet">
<style>
  :root {
    --orange: #efb04d;
    --orange-text: #eea53c;
    --green-dark: #4a7f2f;
    --green-mid: #6f9450;
    --green-light: #97aa77;
    --green-pale: #b9c79e;
    --green-head: #3d7a2c;
    --green-soft: #7c9c5c;
    --cream: #f2f1e8;
    --beige: #e4e1cc;
    --text: #3c3c3c;
    --white: #ffffff;
  }
  * { box-sizing: border-box; margin: 0; padding: 0; }
  html, body { width: 1200px; height: 568px; overflow: hidden; background: var(--white); }
  .flyer {
    position: relative; width: 1200px; height: 568px; overflow: hidden;
    font-family: "Open Sans", sans-serif; color: var(--text);
  }
  .abs { position: absolute; }
  .serif { font-family: "Alegreya", serif; }

  .hero-photo { left: 27px; top: 27px; width: 451px; height: 346px;
    background: linear-gradient(180deg, #b9c7d6 0%, #e9ecee 35%, #eef0ea 55%, #b3ad6e 72%, #7e7a3c 100%); }
  .tagline { left: 0; top: 54px; width: 243px; height: 42px; background: var(--orange);
    color: var(--white); font-family: "Alegreya", serif; font-style: italic; font-size: 13.5px;
    line-height: 15px; text-align: right; padding: 6px 8px 0 0; }

  .theme-box { left: 40px; top: 316px; width: 154px; height: 211px; background: var(--beige); padding: 11px 14px; }
  .theme-box h2 { font-family: "Alegreya", serif; font-weight: 500; font-size: 14.5px; line-height: 14.5px; color: #333; margin-bottom: 3px; }
  .theme-box p { font-size: 9.2px; line-height: 12.4px; margin-bottom: 12px; }

  .path { left: 208px; top: 430px; width: 160px; color: var(--orange-text); }
  .path h3 { font-family: "Alegreya", serif; font-weight: 400; font-size: 14px; margin-bottom: 1px; }
  .path p { font-size: 10.4px; line-height: 13.2px; }

  .info-panel { left: 478px; top: 27px; width: 300px; height: 346px; background: var(--cream); }
  .info-block { left: 527px; width: 235px; }
  .info-block h3 { font-family: "Alegreya", serif; font-weight: 400; font-size: 13.5px; margin-bottom: 4px; }
  .info-block p { font-size: 9.2px; line-height: 12.4px; }
  .h-orange { color: var(--orange-text); }
  .h-green { color: var(--green-head); }

  .topic { width: 106px; height: 87px; text-align: center; padding-top: 9px; font-size: 8.4px; line-height: 10.2px; }
  .topic strong { display: block; font-size: 9px; line-height: 11.5px; margin-bottom: 2px; }
  .t1 { left: 527px; top: 344px; background: var(--green-dark); color: var(--white); }
  .t2 { left: 643px; top: 344px; background: var(--green-mid); color: #eef2e4; padding-top: 12px; }
  .t3 { left: 527px; top: 440px; background: var(--green-light); color: #eef2e4; }
  .t4 { left: 643px; top: 440px; background: var(--green-pale); color: var(--green-dark); }
  .t3, .t4 { padding-top: 19px; }

  .values-title { left: 846px; top: 36px; font-family: "Alegreya", serif; font-size: 14.5px; color: var(--green-head); }
  .chip { top: 76px; height: 32px; background: var(--beige); color: var(--green-head);
    font-size: 8.4px; line-height: 9.5px; text-align: center; padding-top: 7px; }
  .c1 { left: 846px; width: 73px; }
  .c2 { left: 929px; width: 103px; }
  .c3 { left: 1043px; width: 70px; }
  .c4 { left: 1124px; width: 76px; text-align: left; padding-left: 6px; }

  .sprout-photo { left: 805px; top: 122px; width: 238px; height: 142px;
    background: radial-gradient(ellipse at 60% 35%, #c9c35a 0%, #6f8a2a 35%, #2f3d14 70%, #1c1a12 100%); }
  .stance { left: 1043px; top: 122px; width: 116px; height: 142px; background: var(--green-dark); color: var(--white); padding: 18px 0 0 14px; }
  .stance h4 { font-size: 11px; line-height: 13.5px; font-weight: 600; margin-bottom: 2px; }
  .stance ul { list-style: none; font-size: 9.2px; line-height: 12.3px; }
  .stance li { padding-left: 7px; text-indent: -7px; }

  .method { left: 846px; top: 280px; width: 240px; }
  .method h3 { font-family: "Alegreya", serif; font-weight: 400; font-size: 14px; color: var(--green-soft); margin-bottom: 10px; }
  .method p { font-size: 9.2px; line-height: 12.4px; }

  .answer { left: 846px; top: 387px; width: 313px; height: 140px; background: var(--orange); }
  .answer-text { left: 857px; top: 398px; width: 150px; color: var(--white); }
  .answer-text h3 { font-family: "Alegreya", serif; font-weight: 500; font-size: 14px; line-height: 15.5px; margin-bottom: 14px; }
  .answer-text p { font-size: 10.2px; line-height: 13.7px; }
  .portrait-photo { left: 1010px; top: 387px; width: 149px; height: 140px;
    background: linear-gradient(135deg, #bcc7cf 0%, #dfe4e6 45%, #a8b7bf 100%); }
</style>
</head>
<body>
<div class="flyer">
  <div class="abs hero-photo" role="img" aria-label="Foto: zwei Wanderer auf einer Bergwiese unter hellem Himmel"></div>
  <div class="abs tagline">Ein gutes Coachinggespräch ist<br>wie eine gemeinsame Bergtour...</div>

  <div class="abs theme-box">
    <h2>Sie bestimmen das Thema – Ihren Berg.</h2>
    <p>Sie bestimmen das Tempo. Sie entdecken Ihre eigenen Ressourcen während Sie sich Schritt für Schritt Ihrem Ziel nähern.</p>
    <p>Gemeinsam erkunden wir, welche Wege es zu Ihrem Ziel gibt. Ich begleite Sie auf allen Etappen. Ich helfe Ihnen, sich unterwegs zu orientieren.</p>
  </div>

  <div class="abs path">
    <h3>Wir gehen den Weg:</h3>
    <p>mit Offenheit, mit Neugierde, mit einem Lachen, mit einem klaren Blick, mit Pausen, mit Ausdauer, mit Freude, mit Motivation, mit allen Sinnen und allen Emotionen.</p>
  </div>

  <div class="abs info-panel"></div>
  <div class="abs info-block" style="top:46px">
    <h3 class="h-orange">Was ist Coaching &amp; Supervision?</h3>
    <p>Im Coaching und in der Supervision haben Sie die Möglichkeit, Ihr eigenes Handeln im beruflichen Kontext zu reflektieren. Mit Hilfe von strukturierten Gesprächen und ausgewählten Methoden begleite ich Sie dabei, in einem geschützten Rahmen eigene Lösungen zu entwickeln und umzusetzen.</p>
  </div>
  <div class="abs info-block" style="top:177px">
    <h3 class="h-green">Geht es nur um berufliche Themen?</h3>
    <p>Jein. Private Themen können Kraftgeber und Krafträuber sein und sich auf berufliche Themen auswirken. Es geht oft um die Balance im Leben und deshalb ist es gut beides im Auge zu haben. Coaching ist aber keine Therapie.</p>
  </div>
  <div class="abs info-block" style="top:313px">
    <h3 class="h-orange">Häufige Themenfelder:</h3>
  </div>

  <div class="abs topic t1"><strong>Berufliche Kompetenzen</strong>Führung, Umgang mit Veränderungen, herausfordernde Aufgaben meistern</div>
  <div class="abs topic t2"><strong>Persönlichen Kompetenzen</strong>neue Perspektiven, Work-Live-Balance, Konfliktverhalten</div>
  <div class="abs topic t3"><strong>Team</strong>Zusammenarbeit, Kommunikation, Konflikte</div>
  <div class="abs topic t4"><strong>Supervisorische Fallarbeit</strong>schwierige Fälle/ Klienten</div>

  <div class="abs values-title">Coaching &amp; Supervision bedeutet für mich:</div>
  <div class="abs chip c1">Ressourcen<br>Stärken</div>
  <div class="abs chip c2">an Heraus-<br>forderungen wachsen</div>
  <div class="abs chip c3">das Leben<br>gestalten</div>
  <div class="abs chip c4">sich (weiter)<br>entwickeln</div>

  <div class="abs sprout-photo" role="img" aria-label="Foto: junge Pflanzentriebe und eine gelbe Blüte auf dunkler Erde"></div>
  <div class="abs stance">
    <h4>Meine<br>Grundhaltung:</h4>
    <ul>
      <li>• systemisch</li>
      <li>• lösungs- und zielorientiert</li>
      <li>• ressourcen-orientiert</li>
      <li>• wertschätzend</li>
    </ul>
  </div>

  <div class="abs method">
    <h3>Ich habe keine „Beratungsschablonen“.</h3>
    <p>Mir ist wichtig, mit welcher Arbeitsmethode Sie sich wohlfühlen. Deshalb passe ich die Methoden situativ Ihren Bedürfnissen an. Dazu bringe ich einen großen Methodenschatz mit. Besonders wichtig ist mir der Transfer in den Alltag.</p>
  </div>

  <div class="abs answer"></div>
  <div class="abs answer-text">
    <h3>Die Antwort auf<br>Ihre Frage liegt schon<br>in Ihnen...</h3>
    <p>... ich helfe Ihnen, sie zu sehen. Und manchmal helfe ich auch, sich erstmal über die Frage klar zu werden.</p>
  </div>
  <div class="abs portrait-photo" role="img" aria-label="Porträtfoto der Psychologin in heller Bluse"></div>
</div>
</body>
</html>
```